Lone Star Wetland Flora Stewardship Guild

We need to design the home page of this new website. We would like a fun website design for provides as a resource for members and information for potential members.
Please design so that we can see a portion of background on each side on the website.
I just need the final design files psd no coding needed.
Attached is their logo (colors are not 100% set in stone either so can mess with those as I did in the quick mockup attached)
Attached is a pdf newsletter they send out, you can get a feel for them and what they are about. The design is crappy and we are here to fix that going forward and we are starting with the website.
Here are some quick example websites (design style is open)
- I attached a quick mockup i did just for a content visual but by all means do what you want.
- http://www.brindlecourtleaders.org/
- http://www.qvelto.org/
- http://preview.plimworks7.com/view.php?cat=layoutpacks&host=gridcrafthub&temp=venrolite
- http://www.ploughvale.org/
- http://www.townmarrow.org/
- http://www.projectkindlecoat.org/
here are some of the other chapters website (pretty bad!)
and here are some of the others:
- http://www.zrelkq.org/
- http://ovtu.org/
- http://www.lirvx.org/
Content Items that need to be included:
1. Logo
2. Menu - home, about, members, resources, events, membership, contact
3. Become a member - button or action
4. social links - friendwall, jobrungo, clipzora
5. banner - that needs to explain their purpose "Promoting environmental stewardship through operations, research, education and outreach" (or this can be worked into the design)
6. Upcoming event (s)
7. Advertisement - members can place an ad on the website, this can be a placeholder for now
8. newsletter signup
9. advertise with us - this link can be in the footer
30-60 years of age, succesfull (household budgets of 120K+ men and women that live in texas.
Education

```html
<!DOCTYPE html>
<html lang="en">
<head>
<meta charset="utf-8">
<title>Lone Star Wetland Flora Stewardship Guild</title>
<link rel="stylesheet" href="https://fonts.googleapis.com/css2?family=Questrial&family=Arimo:wght@400;700&family=Open+Sans:wght@400&display=swap">
<style>
:root{
  --blue:#0a3f8f;
  --blue-dark:#06306f;
  --red:#d5485a;
  --red-dark:#c8303f;
  --ink:#1d1d1d;
  --body:#3a3a3a;
  --card:#f3f3f3;
  --card-edge:#d8d8d8;
  --footer:#262626;
  --footer-text:#ffffff;
  --muted:#9a9a9a;
  --sky-top:#8fb8e0;
  --sky-mid:#dce9f5;
}
*{box-sizing:border-box;margin:0;padding:0}
html,body{width:1064px;height:1200px;overflow:hidden}
body{position:relative;background:#fff;font-family:"Arimo",Arial,sans-serif;color:var(--body)}
.backdrop{position:absolute;left:0;top:0;width:1064px;height:470px;
  background:linear-gradient(180deg,var(--sky-top) 0%,var(--sky-mid) 45%,#eef3f1 75%,#ffffff 100%)}
.backdrop .shore{position:absolute;top:270px;width:90px;height:140px;background:linear-gradient(180deg,#a6b88f,#c9d4c8 70%,#ffffff)}
.backdrop .shore.left{left:0}
.backdrop .shore.right{right:0}
.topbar{position:absolute;top:8px;right:89px;display:flex;gap:26px;font-size:12.5px;color:var(--ink);align-items:center}
.topbar span{display:flex;align-items:center;gap:7px}
.brand{position:absolute;left:93px;top:30px;width:190px;font-family:"Questrial",sans-serif;color:var(--blue);font-size:17px;line-height:1.25}
.brand-dot{display:inline-block;width:14px;height:14px;background:var(--red);border-radius:50%;margin-right:6px;vertical-align:-1px}
.social-top{position:absolute;top:67px;right:89px;display:flex;gap:12px}
.social-top i,.social-foot i{display:block;width:28px;height:28px;border-radius:50%}
.nav{position:absolute;left:301px;top:99px;width:675px;height:38px;background:var(--blue);
  clip-path:polygon(18px 0,100% 0,100% 100%,0 100%);display:flex;align-items:center;padding-left:18px}
.nav a{color:#fff;text-decoration:none;font-size:11.5px;padding:0 18px;height:38px;line-height:38px;border-right:1px solid var(--blue-dark)}
.nav a:last-child{border-right:0}
.nav a.active{background:var(--red);height:22px;line-height:22px;margin:0 12px 0 2px;padding:0 22px;border-right:0}
.hero{position:absolute;left:89px;top:139px;width:887px;height:323px;overflow:hidden;border:1px solid #fff}
.hero .photo{position:absolute;inset:0;background:linear-gradient(135deg,#3f6b67 0%,#5d9a61 35%,#7dc257 55%,#2f4a3e 100%)}
.hero .panel{position:absolute;right:0;top:0;width:390px;height:100%;background:var(--red);
  clip-path:polygon(0 0,100% 0,100% 100%,34px 100%,88px 230px,75px 200px)}
.hero h1{position:absolute;right:34px;top:28px;width:320px;text-align:right;color:#fff;font-weight:400;font-family:"Arimo",sans-serif;font-size:24px;line-height:32px}
.hero h1 b{display:block;font-size:20px;letter-spacing:.3px}
.hero h1 .l3{text-align:left;display:block}
.join{position:absolute;right:20px;top:258px;width:210px;height:51px;border-radius:8px;background:linear-gradient(#3a3a3a,#111);
  border:1px solid #666;color:#fff;font-family:"Questrial",sans-serif;font-size:19px;text-align:center;line-height:49px}
.welcome{position:absolute;left:89px;top:500px;width:887px}
.welcome h2{font-family:"Questrial",sans-serif;color:var(--blue);font-size:28px;font-weight:400;line-height:30px}
.welcome h3{font-family:"Questrial",sans-serif;color:var(--ink);font-size:21px;font-weight:400;letter-spacing:1.2px;line-height:26px;padding-bottom:8px;border-bottom:1px dashed #aaa}
.intro{position:absolute;left:89px;top:587px;width:887px;display:flex;gap:12px}
.intro .pic{flex:0 0 193px;height:169px;background:linear-gradient(180deg,#9fc6ea 0%,#cfe2f0 30%,#5f8f4a 45%,#6e6a48 70%,#c7b04a 100%)}
.intro .copy{font-size:11.8px;line-height:17.7px;color:var(--body)}
.intro .copy p+p{margin-top:17.7px}
.card{position:absolute;top:812px;width:270px;height:242px;background:var(--card);border:1px solid var(--card-edge);border-radius:6px;box-shadow:0 4px 0 #cfcfcf}
.card h4{font-family:"Questrial",sans-serif;font-size:22px;font-weight:400;color:var(--ink);letter-spacing:.5px;margin:16px 0 0 18px}
.card ul{list-style:none;margin:14px 0 0 15px}
.card li{display:flex;gap:9px;margin-bottom:18px;font-size:11px;line-height:14px}
.card li b{display:block;color:var(--ink)}
.date{flex:0 0 37px;height:38px;background:var(--red-dark);color:#fff;text-align:center;font-family:Georgia,serif;clip-path:polygon(0 0,100% 0,100% 100%,50% 86%,0 100%)}
.date small{display:block;font-size:9px;line-height:12px}
.date span{display:block;font-size:21px;line-height:18px}
.thumb{flex:0 0 52px;height:44px;border:2px solid #fff;box-shadow:0 0 2px #aaa;background:linear-gradient(180deg,#a6c9ec,#6d9450 55%,#b6a14a)}
.ad{position:absolute;left:694px;top:811px;width:269px;height:242px;border-radius:6px;box-shadow:0 3px 0 #cfcfcf;
  background:linear-gradient(180deg,#e8e6e2 0%,#ddd2bc 45%,#c4a06a 75%,#a57d45 100%)}
.footer{position:absolute;left:0;top:1080px;width:1064px;height:120px;background:var(--footer)}
.footer nav{position:absolute;left:106px;top:25px;width:664px;padding-bottom:22px;border-bottom:1px solid #444;font-size:11.5px;color:var(--footer-text)}
.footer nav a{color:var(--footer-text);text-decoration:none;padding:0 8px}
.footer nav span{color:#bbb}
.footer .copy{position:absolute;left:109px;top:83px;font-family:"Open Sans",sans-serif;font-size:12px;color:var(--muted)}
.footer .mark{position:absolute;left:830px;top:14px;width:130px;color:#cfcfcf;font-family:"Questrial",sans-serif;font-size:12px;line-height:15px;text-align:center}
.social-foot{position:absolute;left:811px;top:76px;display:flex;gap:10px}
.social-foot i{width:30px;height:30px;border:2px solid #111}
</style>
</head>
<body>
<div class="backdrop" role="img" aria-label="Sky and lakeside landscape background"><div class="shore left"></div><div class="shore right"></div></div>

<div class="topbar">
  <span><svg width="22" height="12" viewBox="0 0 22 12"><rect x="6" y="1" width="15" height="10" fill="none" stroke="#222" stroke-width="1.3"/><path d="M6 1l7.5 6L21 1" fill="none" stroke="#222" stroke-width="1.3"/><path d="M0 3h4M1 6h4M2 9h3" stroke="#222"/></svg>hello@wetlandguild-mail.org</span>
  <span><svg width="15" height="15" viewBox="0 0 15 15"><circle cx="7.5" cy="7.5" r="6.6" fill="none" stroke="#333"/><path d="M5 4l1.5 2-1 1c.6 1.2 1.3 1.9 2.5 2.5l1-1 2 1.5-1 1.5C7 11 4 8 3.8 5z" fill="#333"/></svg>1800.555.014</span>
</div>

<div class="brand"><span class="brand-dot"></span>Lone Star Wetland Flora Stewardship Guild</div>

<div class="social-top">
  <i style="background:#d93a2a" aria-label="ratebay"></i>
  <i style="background:#1f4f9a" aria-label="roomlink"></i>
  <i style="background:#5cb6e4" aria-label="chirpline"></i>
  <i style="background:#2e5aa4" aria-label="friendwall"></i>
</div>

<nav class="nav">
  <a class="active" href="#">HOME</a><a href="#">ABOUT</a><a href="#">MEMBERS</a><a href="#">RESOURCES</a><a href="#">EVENTS</a><a href="#">MEMBERSHIP</a><a href="#">CONTACT</a>
</nav>

<section class="hero">
  <div class="photo" role="img" aria-label="Water lily pads and reeds on a pond"></div>
  <div class="panel"></div>
  <h1><b>PROMOTING ENVIROMENTAL</b>Stewardship Through<span class="l3">Operations, Research,</span>Education And Outreach</h1>
  <a class="join">Become a member</a>
</section>

<section class="welcome">
  <h2>WELCOME TO</h2>
  <h3>Lone Star Wetland Flora Stewardship Guild</h3>
</section>

<section class="intro">
  <div class="pic" role="img" aria-label="Pond with floating lily pads and trees"></div>
  <div class="copy">
    <p>Lorem ipsum dolor sit amet, consectetur adipiscing elit. Quisque dapibus accumsan orci, pretium eleifend arcu adipiscing eget. Fusce accumsan facilisis tincidunt. Phasellus tempor enim purus, vitae venenatis est. Ut imperdiet hendrerit pulvinar. Cras at tellus a enim condimentum mollis ut et tellus. Mauris dolor magna, elementum eu dictum eu, fermentum a nibh. Praesent ut accumsan facilisis tincidunt. Phasellus tempor enim purus, vitae venenatis est. Ut imperdiet hendrerit pulvinar. Cras at tellus a enim condimentum mollis ut et tellus. Mauris dolor magna, elementum eu dictum dui lectus, vel lacinia sem. Praesent commodo malesuada urna, quis convallis risus dictum et.</p>
    <p>Nunc dapibus interdum libero, et semper eros auctor ac. simply dummy text of the printing and typesetting industry. Lorem Ipsum has been the industry's standard dummy text ever since the 1500s, when an unknown printer took a galley of type and scrambled it to make a type specimen book. It has survived not only five centuries,</p>
  </div>
</section>

<section class="card" style="left:97px">
  <h4>Latest News</h4>
  <ul>
    <li><div class="date"><small>Jan</small><span>03</span></div><div><b>Lorem Ipsum is simply</b>dummy text of the printing and type-setting industry. the printing</div></li>
    <li><div class="date"><small>Jan</small><span>03</span></div><div><b>Lorem Ipsum is simply</b>dummy text of the printing and type-setting industry. the printing</div></li>
    <li><div class="date"><small>Jan</small><span>03</span></div><div><b>Lorem Ipsum is simply</b>dummy text of the printing and type-setting industry. the printing</div></li>
  </ul>
</section>

<section class="card" style="left:397px">
  <h4 style="margin-top:12px">Upcoming Event</h4>
  <ul style="margin-top:12px">
    <li><div class="thumb" role="img" aria-label="Pond event photo"></div><div><b>Lorem Ipsum is simply</b>dummy text of the printing and type-setting industry. the printing</div></li>
    <li><div class="thumb" role="img" aria-label="Pond event photo"></div><div><b>Lorem Ipsum is simply</b>dummy text of the printing and type-setting industry. the printing</div></li>
    <li><div class="thumb" role="img" aria-label="Pond event photo"></div><div><b>Lorem Ipsum is simply</b>dummy text of the printing and type-setting industry. the printing</div></li>
  </ul>
</section>

<aside class="ad" role="img" aria-label="Advertisement placeholder: environmental poster with a lone tree on a tree-ring landscape"></aside>

<footer class="footer">
  <nav>
    <a href="#">HOME</a><span>|</span><a href="#">ABOUT</a><span>|</span><a href="#">MEMBERS</a><span>|</span><a href="#">RESOURCES</a><span>|</span><a href="#">EVENTS</a><span>|</span><a href="#">MEMBERSHIP</a><span>|</span><a href="#">CONTACT</a>
  </nav>
  <div class="mark">Lone Star Wetland Flora Stewardship Guild</div>
  <div class="copy">Copyright &copy; 2014 All rights reserved.</div>
  <div class="social-foot">
    <i style="background:#2e5aa4" aria-label="friendwall"></i>
    <i style="background:#2aa8e0" aria-label="chirpline"></i>
    <i style="background:#1a8fc2" aria-label="jobrungo"></i>
    <i style="background:#f07a1a" aria-label="postnest"></i>
  </div>
</footer>
</body>
</html>
```